Roofing Company needs YOU to help put us on top!

Brightpeak Roofing, a fresh new company with quality and Innovation in mind, needs your help to stand out in the competitive Chicago market. With over 30 years of experience, all the right people and tools for the job, the only thing we are missing is your creative ideas in web design to help us grow our online presence.
Our Company offers exceptional quality at reasonable prices, we work for the everyday people both blue collar and white collar.

We have used Craftswarm in the past with multiple successful campaigns, we are excited to see what you can come up with for our website.

www.BrightpeakRoofing.example will be the domain

We will be hiring a photographer for visual content on our pages later. Stock photos are okay to use but should follow theme.

Thank you for taking the time on the submissions, if you have any questions don't hesitate to ask and we will provide whatever is needed to you.

Target Market(s)

Homeowners & Commercial Clients between 21-65

Industry/Entity Type

Roofing

Coding

Coded - Design and coding required

Number of Pages Required

4 page

Font styles to use
Sans Serif

Colors
ffffff
ec1f27
000000
5c5c5c
757575
b2b2b2

Requirements
Must have
• Color Scheme - should follow around our logo
• As for pages we were looking for an About, Services, Projects (gallery page) and Contact.
• Main page please include social media links and a a place so people could use tillbee to make payments
• Website should work on desktop as well as mobile platforms
Nice to have
• A Live chat feature would be nice if possible
Should not have
• Obscure Colors or Common web templates

```html
<!DOCTYPE html>
<html lang="en">
<head>
<meta charset="utf-8">
<title>Brightpeak Roofing</title>
<link href="https://fonts.googleapis.com/css2?family=Raleway:wght@300;400;500;600;700;800&family=Open+Sans:wght@400;600&display=swap" rel="stylesheet">
<style>
:root{
  --red:#ec1f27;
  --black:#000000;
  --ink:#333333;
  --grey-dark:#5c5c5c;
  --grey:#757575;
  --grey-light:#b2b2b2;
  --white:#ffffff;
  --panel:#f3f3f3;
  --footer:#1c1c1c;
  --footer-bar:#262626;
  --head:"Raleway",Arial,sans-serif;
  --body:"Open Sans",Arial,sans-serif;
}
*{box-sizing:border-box;margin:0;padding:0}
html,body{width:1200px;height:2302px;overflow:hidden;background:var(--white)}
body{position:relative;font-family:var(--body);color:var(--grey-dark)}
.abs{position:absolute}

/* header */
.site-header{position:absolute;left:0;top:0;width:1200px;height:103px;background:var(--white);box-shadow:0 2px 4px rgba(0,0,0,.15);z-index:2}
.brand{position:absolute;left:153px;top:20px;width:175px;text-align:center}
.brand-name{font-family:var(--head);font-weight:800;font-size:19px;color:var(--black);letter-spacing:.2px;white-space:nowrap}
.brand-phone{font-family:var(--head);font-weight:800;font-size:14px;color:var(--black);margin-top:4px;letter-spacing:.5px}
.main-nav a{position:absolute;top:44px;font-family:var(--body);font-size:16px;color:var(--ink);text-decoration:none;white-space:nowrap}
.main-nav a.active{color:var(--red)}
.nav-underline{position:absolute;left:379px;top:98px;width:70px;height:5px;background:var(--red)}
.live-chat{position:absolute;left:895px;top:35px;width:150px;height:37px;background:var(--red);border-radius:2px;color:var(--white);font-family:var(--body);font-size:13px;display:flex;align-items:center;justify-content:center;gap:6px}

/* hero */
.hero{position:absolute;left:0;top:103px;width:1200px;height:480px;overflow:hidden}
.hero-photo{position:absolute;inset:0;background:linear-gradient(160deg,#8a8f96 0%,#6d6a68 35%,#5a4038 65%,#3b2a25 100%)}
.hero-shade{position:absolute;inset:0;background:rgba(0,0,0,.18)}
.hero-title{position:absolute;left:0;top:152px;width:1200px;text-align:center;font-family:var(--head);font-weight:600;font-size:48px;color:var(--white);letter-spacing:.5px}
.hero-sub{position:absolute;left:0;top:216px;width:1200px;text-align:center;font-family:var(--head);font-weight:600;font-size:27px;color:var(--white)}
.hero-btn{position:absolute;left:534px;top:261px;width:149px;height:41px;border:2px solid var(--white);color:var(--white);font-family:var(--head);font-weight:600;font-size:15px;display:flex;align-items:center;justify-content:center}
.hero-dots{position:absolute;left:560px;top:440px;display:flex;gap:5px}
.hero-dots span{width:17px;height:17px;border-radius:50%;background:var(--white)}
.hero-dots span.current{background:transparent;border:2px solid var(--white)}

/* about */
.about{position:absolute;left:0;top:583px;width:1200px;height:270px;background:var(--white);text-align:center}
.section-title{font-family:var(--head);font-weight:400;font-size:27px;color:var(--ink)}
.about .section-title{position:absolute;left:0;top:52px;width:1200px}
.about p{position:absolute;left:176px;top:101px;width:848px;font-size:14.5px;line-height:31px;color:var(--grey)}

/* services */
.services{position:absolute;left:0;top:853px;width:1200px;height:353px;overflow:hidden}
.services-photo{position:absolute;inset:0;background:linear-gradient(100deg,#3c4048 0%,#6a6560 40%,#8a7f72 60%,#4a4a4e 100%)}
.services-shade{position:absolute;inset:0;background:rgba(20,20,20,.45)}
.service{position:absolute;top:39px;width:260px;text-align:center;color:var(--white)}
.service svg{display:block;margin:0 auto}
.service h3{font-family:var(--body);font-weight:400;font-size:17.5px;margin-top:22px;letter-spacing:.3px}
.service p{font-size:12px;line-height:19px;color:#c9c9c9;margin-top:6px}
.service .outline-btn{display:inline-flex;margin-top:16px;width:110px;height:34px;border:1.5px solid var(--white);align-items:center;justify-content:center;font-size:11.5px;font-weight:600}

/* why choose us */
.why{position:absolute;left:0;top:1206px;width:1200px;height:387px;background:var(--panel);overflow:hidden;border-bottom:1px solid #dcdcdc}
.why-photo{position:absolute;left:506px;top:0;width:694px;height:387px;background:linear-gradient(180deg,#6fa3dc 0%,#a8c9ea 45%,#b0724c 60%,#8a4e33 100%)}
.why-fade{position:absolute;left:506px;top:0;width:160px;height:387px;background:linear-gradient(90deg,var(--panel),rgba(243,243,243,0))}
.why h2{position:absolute;left:158px;top:78px;font-family:var(--head);font-weight:400;font-size:35px;color:var(--ink)}
.why .lead{position:absolute;left:158px;top:134px;width:400px;font-size:14.5px;line-height:23px;color:var(--ink)}
.why .detail{position:absolute;left:158px;top:186px;width:400px;font-size:12px;line-height:21.5px;color:var(--grey-dark)}
.red-btn{position:absolute;left:158px;top:267px;width:115px;height:34px;background:var(--red);border-radius:3px;color:var(--white);font-size:12.5px;display:flex;align-items:center;justify-content:center;gap:6px}

/* projects */
.projects{position:absolute;left:0;top:1593px;width:1200px;height:408px;background:var(--white)}
.projects h2{position:absolute;left:153px;top:52px;font-family:var(--head);font-weight:400;font-size:28px;color:var(--red)}
.project-card{position:absolute;top:104px;width:208px;height:235px;border:1px solid #d4d4d4;background:linear-gradient(180deg,#ffffff 50%,#eeeeee 100%)}
.project-image{height:124px}
.project-card h3{font-family:var(--body);font-weight:400;font-size:15px;color:var(--ink);margin:13px 0 0 19px}
.project-card p{font-size:11.5px;line-height:20px;color:var(--grey);margin:4px 0 0 19px;width:180px}
.project-card .more{font-size:11px;font-weight:600;color:var(--red);margin:2px 0 0 19px}

/* footer */
.site-footer{position:absolute;left:0;top:2001px;width:1200px;height:249px;background:var(--footer)}
.footer-col{position:absolute;top:50px}
.footer-col h4{font-family:var(--head);font-weight:400;font-size:16px;color:var(--white);letter-spacing:.3px}
.footer-col ul{list-style:none;margin-top:11px}
.footer-col li{font-size:11.5px;line-height:23px;color:#d8d8d8}
.footer-divider{position:absolute;top:45px;width:1px;height:150px;background:#333333}
.contact-line{display:flex;align-items:center;gap:8px}
.pay-row{display:flex;gap:12px;margin-top:12px}
.pay-row span{width:34px;height:22px;background:#d7d7d7;border-radius:2px}
.social{display:flex;gap:4px;margin-top:10px}
.social span{width:30px;height:30px;border:1.5px solid var(--white);border-radius:50%}
.footer-bar{position:absolute;left:0;top:2250px;width:1200px;height:52px;background:var(--footer-bar);text-align:center;font-size:11.5px;line-height:52px;color:#a0a0a0}
</style>
</head>
<body>

<header class="site-header">
  <div class="brand">
    <div class="brand-name">Brightpeak Roofing</div>
    <div class="brand-phone">708-555-0142</div>
  </div>
  <nav class="main-nav">
    <a class="active" style="left:387px">HOME</a>
    <a style="left:468px">ABOUT</a>
    <a style="left:557px">SERVICES</a>
    <a style="left:666px">PROJECTS</a>
    <a style="left:780px">CONTACT US</a>
  </nav>
  <div class="nav-underline"></div>
  <div class="live-chat">
    <svg width="18" height="16" viewBox="0 0 18 16" aria-hidden="true"><path d="M2 2h14v9H7l-4 3v-3H2z" fill="none" stroke="#fff" stroke-width="1.6" stroke-linejoin="round"/></svg>
    LIVE CHAT NOW
  </div>
</header>

<section class="hero">
  <div class="hero-photo" role="img" aria-label="Roofer in a safety vest nailing shingles on a pitched roof"></div>
  <div class="hero-shade"></div>
  <h1 class="hero-title">ROOFING &amp; GUTTER SERVICE</h1>
  <div class="hero-sub">MAECENAS ALIQUET VELIT VEL TURPIS</div>
  <div class="hero-btn">LEARN MORE</div>
  <div class="hero-dots"><span class="current"></span><span></span><span></span><span></span></div>
</section>

<section class="about">
  <h2 class="section-title">ABOUT OUR COMPANY</h2>
  <p>Duis sed tellus et tortor vestibulum gravida Praesent elementum elit at tellus Curabitur metus ipsum luctus eu malesuada ut tincidunt sed diam Donec quis mi sed magna hendrerit accumsan Suspendisse risus nibh ultricies eu volutpat non condimentum hendrerit augue Etiam eleifend metus vitae adipiscing semper mauris ipsum iaculis</p>
</section>

<section class="services">
  <div class="services-photo" role="img" aria-label="Close view of hands working on roof timber"></div>
  <div class="services-shade"></div>

  <div class="service" style="left:185px">
    <svg width="116" height="132" viewBox="0 0 116 132" aria-hidden="true">
      <polygon points="58,2 114,33 114,99 58,130 2,99 2,33" fill="var(--red)"/>
      <polygon points="58,36 28,60 88,60" fill="#fff"/>
      <rect x="36" y="60" width="44" height="26" fill="#fff"/>
      <rect x="52" y="70" width="12" height="16" fill="var(--red)"/>
    </svg>
    <h3>ROOFING</h3>
    <p>Maecenas aliquet velit vel turpis Mauris neque<br>metus malesuada nec ultricies sit</p>
    <div class="outline-btn">READ MORE</div>
  </div>

  <div class="service" style="left:468px">
    <svg width="116" height="132" viewBox="0 0 116 132" aria-hidden="true">
      <polygon points="58,2 114,33 114,99 58,130 2,99 2,33" fill="var(--red)"/>
      <line x1="50" y1="78" x2="74" y2="38" stroke="#fff" stroke-width="4" stroke-linecap="round"/>
      <path d="M32 76h52a4 4 0 0 1 0 8 26 10 0 0 1-52 0z" fill="#fff"/>
    </svg>
    <h3>GUTTERS</h3>
    <p>Maecenas aliquet velit vel turpis Mauris neque<br>metus malesuada nec ultricies sit</p>
    <div class="outline-btn">READ MORE</div>
  </div>

  <div class="service" style="left:755px">
    <svg width="116" height="132" viewBox="0 0 116 132" aria-hidden="true">
      <polygon points="58,2 114,33 114,99 58,130 2,99 2,33" fill="var(--red)"/>
      <rect x="46" y="36" width="24" height="24" rx="2" fill="#fff"/>
      <path d="M38 64h40a20 16 0 0 1-20 16z" fill="#fff"/>
      <rect x="50" y="78" width="16" height="14" fill="#fff"/>
    </svg>
    <h3>KITCHEN &amp; BATHS</h3>
    <p>Maecenas aliquet velit vel turpis Mauris neque<br>metus malesuada nec ultricies sit</p>
    <div class="outline-btn">READ MORE</div>
  </div>
</section>

<section class="why">
  <div class="why-photo" role="img" aria-label="Brick house with open roof framing and roofers on the rafters under a blue sky"></div>
  <div class="why-fade"></div>
  <h2>Why Choose Us</h2>
  <p class="lead">Mauris vel lacus vitae felis vestibulum volutpat E eu imperdiet ac nisl Cum sociis natoque penatibus et magnis</p>
  <p class="detail">montes nascetur ridiculus mus In iaculis facilisis massa Etiam eu urna Sed porta Suspendisse quam leo molestie sed luctus quis eugiat in pede Fusce tellus Sed metus augue convallis et vehicula ut pulvinar</p>
  <div class="red-btn">READ MORE
    <svg width="7" height="10" viewBox="0 0 7 10" aria-hidden="true"><path d="M1 1l4 4-4 4" fill="none" stroke="#fff" stroke-width="1.5"/></svg>
  </div>
</section>

<section class="projects">
  <h2>Latest Projects</h2>

  <article class="project-card" style="left:157px">
    <div class="project-image" role="img" aria-label="House under construction with bare roof framing" style="background:linear-gradient(180deg,#7fb0e0 0%,#b9d3ee 45%,#a86a45 75%,#7a4a32 100%)"></div>
    <h3>Massa est sed nisl</h3>
    <p>Class aptent taciti sociosqu ad litora torquent per conubia</p>
    <div class="more">READ MORE</div>
  </article>

  <article class="project-card" style="left:382px">
    <div class="project-image" role="img" aria-label="Brick house with a new dark shingle roof" style="background:linear-gradient(180deg,#dfe6ee 0%,#4c4f55 40%,#8a5a44 75%,#6e4838 100%)"></div>
    <h3>Etiam eleifend metus</h3>
    <p>Class aptent taciti sociosqu ad litora torquent per conubia</p>
    <div class="more">READ MORE</div>
  </article>

  <article class="project-card" style="left:609px">
    <div class="project-image" role="img" aria-label="Gloved hand clearing leaves from a roof gutter" style="background:linear-gradient(160deg,#6e6a62 0%,#8c7a55 45%,#5d7a3a 75%,#3f4a2c 100%)"></div>
    <h3>Aliquam nec erat at</h3>
    <p>Class aptent taciti sociosqu ad litora torquent per conubia</p>
    <div class="more">READ MORE</div>
  </article>

  <article class="project-card" style="left:833px">
    <div class="project-image" role="img" aria-label="Renovated modern bathroom with grey tiles" style="background:linear-gradient(160deg,#8a8a8c 0%,#5a5a5e 45%,#3a3634 75%,#6a625a 100%)"></div>
    <h3>Pellentesque rutrum</h3>
    <p>Class aptent taciti sociosqu ad litora torquent per conubia</p>
    <div class="more">READ MORE</div>
  </article>
</section>

<footer class="site-footer">
  <div class="footer-col" style="left:158px">
    <h4>COMPANY</h4>
    <ul><li>Home</li><li>About Us</li><li>Our Projects</li><li>Our Team</li></ul>
  </div>
  <div class="footer-divider" style="left:276px"></div>
  <div class="footer-col" style="left:305px">
    <h4>SUBLINKS</h4>
    <ul><li>Our Services</li><li>Solution</li><li>Clients</li><li>Projects</li></ul>
  </div>
  <div class="footer-divider" style="left:434px"></div>
  <div class="footer-col" style="left:466px">
    <h4>RESOURCES</h4>
    <ul><li>Our Partners</li><li>Career</li><li>Term of Use</li><li>Contact Us</li></ul>
  </div>
  <div class="footer-divider" style="left:592px"></div>
  <div class="footer-col" style="left:620px">
    <h4>CONTACT INFO</h4>
    <ul>
      <li>410 Ridge Line Avenue Suite B12</li>
      <li class="contact-line">
        <svg width="12" height="12" viewBox="0 0 12 12" aria-hidden="true"><path d="M3 1l2 2.5-1.2 1.3a7 7 0 0 0 3.4 3.4L8.5 7 11 9l-1 2C5 11 1 7 1 2z" fill="#fff"/></svg>
        (312) 555-0178</li>
      <li class="contact-line">
        <svg width="12" height="10" viewBox="0 0 12 10" aria-hidden="true"><rect x="0.5" y="0.5" width="11" height="9" fill="#fff"/><path d="M1 1l5 4 5-4" fill="none" stroke="#1c1c1c" stroke-width="1.2"/></svg>
        info@brightpeakroofing.example</li>
    </ul>
    <div class="pay-row" aria-label="Accepted payments including tillbee"><span></span><span></span><span></span><span></span><span></span></div>
  </div>
  <div class="footer-divider" style="left:864px"></div>
  <div class="footer-col" style="left:898px">
    <h4>FOLLOW US</h4>
    <div class="social" aria-label="Social media links"><span></span><span></span><span></span><span></span></div>
  </div>
</footer>
<div class="footer-bar">© 2016 Company Name&nbsp; All right reserved</div>

</body>
</html>
```